Seven Lanterns at Dusk.

I need a book cover (and back cover) design for a novel. The novel is a thiller. ´Synopsis: During the party after an awards ceremony at prestigious institution, one of the young awarders dissapear. The last place where he left a trace was close to a giant chessboard in the grass of the beautiful gardens of the place of ceremony. The detective in charge of finding the missing person and find out what happened will gradually discover that the institution is not all that it seems.
The book cover size will be 9" x 6" and the title of the novel "Seven lanterns at dusk" will be name in spanish "Siete faroles al anochecer". The back cover will have a synopsis (in spanish )that i will develop later on.
One suggestion for the design: I always love the art of OTTO PEMBERLY for movie posters, so I´m looking for something of similar style, you know (a widow beside copper rails, Harbor lamp waltz, mirrowen, ledger of silence, etc

```html
<!DOCTYPE html>
<html lang="es">
<head>
<meta charset="utf-8">
<title>Siete faroles al anochecer — cubierta</title>
<link href="https://fonts.googleapis.com/css2?family=Montserrat:ital,wght@0,500;0,700;1,300&family=Poppins:wght@300;400&display=swap" rel="stylesheet">
<style>
  :root {
    --backdrop: #d6d6d6;
    --cover-red: #c41f26;
    --leaf-red: #a8161c;
    --ink: #0a0a0a;
    --paper: #ffffff;
    --title-font: "Montserrat", sans-serif;
    --body-font: "Poppins", sans-serif;
  }
  * { box-sizing: border-box; margin: 0; padding: 0; }
  html, body { width: 800px; height: 1200px; overflow: hidden; background: var(--backdrop); }
  .spread { position: absolute; left: 20px; top: 343px; width: 760px; height: 513px; }
  .panel {
    position: absolute; top: 0; height: 513px; overflow: hidden;
    background: var(--cover-red);
    box-shadow: 2px 3px 6px rgba(0,0,0,.25);
  }
  .panel--back { left: 0; width: 343px; }
  .panel--spine { left: 352px; width: 57px; }
  .panel--front { left: 417px; width: 343px; }

  .foliage {
    position: absolute; left: 0; top: 0; width: 100%; height: 120px;
    background: linear-gradient(180deg, rgba(150,18,24,.55), rgba(196,31,38,0));
  }
  .ground {
    position: absolute; left: 0; top: 355px; width: 100%; height: 158px;
    background: linear-gradient(180deg, rgba(10,10,10,0) 0, var(--ink) 28px);
  }
  .bottom-stripe {
    position: absolute; left: 0; top: 488px; width: 100%; height: 6px;
    background: var(--cover-red);
  }

  .title { position: absolute; left: 0; width: 100%; text-align: center; font-family: var(--title-font); color: var(--paper); }
  .title__top { font-weight: 700; letter-spacing: .5px; line-height: 1; }
  .title__box {
    display: inline-flex; align-items: baseline; gap: 8px;
    background: var(--ink); font-weight: 700; line-height: 1;
  }
  .title__small { font-weight: 300; font-style: italic; }

  /* Front */
  .panel--front .title { top: 122px; }
  .panel--front .title__top { font-size: 27px; }
  .panel--front .title__box { margin-top: 6px; padding: 6px 10px 7px; font-size: 24px; }
  .panel--front .title__small { font-size: 15px; }
  .hero-art {
    position: absolute; left: 40px; top: 232px; width: 263px; height: 150px;
    background: radial-gradient(ellipse at 50% 70%, #1a0a0b 0 45%, rgba(140,16,22,.9) 70%, rgba(196,31,38,0) 100%);
  }
  .tagline {
    position: absolute; left: 40px; top: 418px; width: 263px;
    font-family: var(--body-font); font-weight: 300; font-size: 7px; line-height: 11px;
    color: var(--paper); text-align: center;
  }
  .author-name {
    position: absolute; left: 0; top: 463px; width: 100%; text-align: center;
    font-family: var(--title-font); font-weight: 500; font-size: 11px; letter-spacing: .5px; color: var(--paper);
  }

  /* Back */
  .panel--back .title { top: 40px; }
  .panel--back .title__top { font-size: 20px; }
  .panel--back .title__box { margin-top: 4px; padding: 4px 8px 5px; font-size: 18px; }
  .panel--back .title__small { font-size: 11px; }
  .synopsis, .bio {
    position: absolute; left: 26px; width: 291px;
    font-family: var(--body-font); font-weight: 300; font-size: 6.8px; line-height: 10.1px;
    color: var(--paper); text-align: justify;
  }
  .synopsis { top: 122px; }
  .bio-heading {
    position: absolute; left: 0; top: 199px; width: 100%; text-align: center;
    font-family: var(--title-font); font-weight: 500; font-size: 9px; letter-spacing: .4px; color: var(--paper);
  }
  .bio { top: 217px; }
  .bio__portrait { float: left; width: 62px; height: 71px; margin: 3px 17px 4px 0; background: var(--paper); }

  /* Spine */
  .spine-title {
    position: absolute; left: 0; top: 52px; width: 100%;
    display: flex; flex-direction: column; align-items: center;
  }
  .spine-title__top, .spine-title__box {
    writing-mode: vertical-rl; font-family: var(--title-font); font-weight: 700; color: var(--paper); line-height: 1;
  }
  .spine-title__top { font-size: 15px; letter-spacing: .5px; }
  .spine-title__box {
    margin-top: 8px; background: var(--ink); padding: 6px 4px; font-size: 15px;
    display: flex; align-items: center; gap: 6px;
  }
  .spine-title__box .title__small { font-size: 8px; }
  .spine-author {
    position: absolute; left: 0; top: 405px; width: 100%;
    display: flex; justify-content: center;
  }
  .spine-author span {
    writing-mode: vertical-rl; font-family: var(--title-font); font-weight: 500;
    font-size: 7px; letter-spacing: .4px; color: var(--paper);
  }
</style>
</head>
<body>
<main class="spread">

  <section class="panel panel--back" aria-label="Contracubierta">
    <div class="foliage" role="img" aria-label="Follaje de bambú en rojo oscuro"></div>
    <div class="ground" role="img" aria-label="Silueta de hierba sobre fondo negro"></div>
    <div class="bottom-stripe"></div>
    <h2 class="title">
      <span class="title__top">SIETE FAROLES</span><br>
      <span class="title__box"><span class="title__small">al</span>ANOCHECER</span>
    </h2>
    <p class="synopsis">Lorem Ipsum is simply dummy text of the printing and typesetting industry. Lorem Ipsum has been the industry's standard dummy text ever since the 1500s, when an unknown printer took a galley of type and scrambled it to make a type specimen book. It has survived not only five centuries, but also the leap into electronic typesetting, remaining essentially unchanged. It was popularised in the 1960s with the release of Quillset</p>
    <h3 class="bio-heading">ABOUT THE AUTHOR</h3>
    <p class="bio"><span class="bio__portrait" role="img" aria-label="Retrato del autor"></span>Lorem Ipsum is simply dummy text of the printing and typesetting industry. Lorem Ipsum has been the industry's standard dummy text ever since the 1500s, when an unknown printer took a galley of type and scrambled it to make a type specimen book. It has survived not only five centuries, but also the leap into electronic typesetting, remaining essentially unchanged. It was popularised in the 1960s with the release of Quillset. Lorem Ipsum is simply dummy text of the printing and typesetting industry. Lorem Ipsum has been the industry's standard dummy text ever since the 1500s, when an unknown printer took a galley of type and scrambled it to make a type specimen book. It has survived not only five centuries, but also the leap into electronic typesetting, remaining essentially unchanged. It was popularised in the 1960s with the release of Quillset</p>
  </section>

  <section class="panel panel--spine" aria-label="Lomo">
    <div class="foliage" role="img" aria-label="Follaje de bambú en rojo oscuro"></div>
    <div class="ground" role="img" aria-label="Silueta de hierba sobre fondo negro"></div>
    <div class="bottom-stripe"></div>
    <div class="spine-title">
      <span class="spine-title__top">SIETE FAROLES</span>
      <span class="spine-title__box"><span class="title__small">al</span>ANOCHECER</span>
    </div>
    <div class="spine-author"><span>MARCEL DOVRANO</span></div>
  </section>

  <section class="panel panel--front" aria-label="Cubierta">
    <div class="foliage" role="img" aria-label="Follaje de bambú en rojo oscuro"></div>
    <div class="hero-art" role="img" aria-label="Siluetas de piezas de ajedrez gigantes y un detective entre arbustos del jardín"></div>
    <div class="ground" role="img" aria-label="Silueta de hierba sobre fondo negro"></div>
    <div class="bottom-stripe"></div>
    <h1 class="title">
      <span class="title__top">SIETE FAROLES</span><br>
      <span class="title__box"><span class="title__small">al</span>ANOCHECER</span>
    </h1>
    <p class="tagline">Lorem Ipsum is simply dummy text of the printing and typesetting industry. Lorem Ipsum has been the industry's Lorem Ipsum is simply dummy text of the printing and typesetting industry. L</p>
    <p class="author-name">MARCEL DOVRANO</p>
  </section>

</main>
</body>
</html>
```